Gaming Website - fragvault.co.uk

I have an existing website www.fragvault.co.uk, I'd like to have it redesigned so it has more of a gaming feel to it. Something along the lines of similar websites:

www.lomantix.org
www.vyrndash.com
www.bemkroft.com
www.quidlane.com
www.pv-racking.com
www.hornbeamtactics.com

Target Market(s)

Gamers - First Person Shooter

Requirements
Must have
• Internal page: sidebar, form and a table with data

```html
<!DOCTYPE html>
<html lang="en">
<head>
<meta charset="utf-8">
<title>FragVault – Registration</title>
<link href="https://fonts.googleapis.com/css2?family=Arimo:wght@400;700&display=swap" rel="stylesheet">
<style>
:root{
  --bg:#000;
  --panel:#2a2a2a;
  --panel-inner:#121212;
  --blue:#2aa8dc;
  --blue-light:#5cc8ef;
  --text:#e6e6e6;
  --muted:#bdbdbd;
  --field:#fbf7f8;
  --rule:#555;
}
*{box-sizing:border-box;margin:0;padding:0}
html,body{width:1200px;height:900px;overflow:hidden;background:var(--bg);font-family:"Arimo",Arial,sans-serif;color:var(--text)}
.abs{position:absolute}
.topbar{left:0;top:0;width:1200px;height:42px;background:linear-gradient(#2a2a2a,#0c0c0c);border-bottom:1px solid #3a3a3a;font-size:11px}
.topbar span,.topbar a{position:absolute;top:13px;color:#fff;text-decoration:none}
.top-field{position:absolute;top:12px;height:17px;background:#fff;border:1px solid #999}
.login-btn{position:absolute;left:590px;top:12px;width:57px;height:17px;background:linear-gradient(var(--blue-light),var(--blue));color:#fff;font-weight:700;font-size:11px;text-align:center;line-height:17px;border-radius:2px}
.hero{left:280px;top:43px;width:810px;height:170px;background:radial-gradient(ellipse at 45% 40%,#5a5a4a 0%,#2a2a24 35%,#0b0b0b 75%)}
.logo{left:122px;top:70px;display:flex;align-items:center;gap:10px}
.logo-name{font-size:34px;font-weight:700;color:#e8e8e8;letter-spacing:1px}
.logo-mark{width:18px;height:18px;background:#e8e8e8}
.tagline{left:253px;top:119px;font-size:12px;font-weight:700;color:#fff}
.search{left:700px;top:77px;width:390px;height:48px;background:#1a1a1a;border:1px solid #444;border-radius:3px}
.search-input{position:absolute;left:10px;top:11px;width:295px;height:25px;background:#fff;color:#888;font-size:10px;font-weight:700;padding:7px 10px}
.search-btn{position:absolute;left:305px;top:11px;width:74px;height:25px;background:linear-gradient(var(--blue-light),var(--blue));color:#fff;font-weight:700;font-size:12px;text-align:center;line-height:25px}
.nav{left:110px;top:158px;width:980px;height:40px;background:linear-gradient(#3c3c3c,#151515);border:1px solid #444;display:flex;align-items:center;font-size:12px;font-weight:700}
.nav-item{padding:0 30px;height:40px;line-height:38px;border-right:1px solid #444;color:#fff}
.nav-item:last-of-type{border:none}
.caret{display:inline-block;border:4px solid transparent;border-top:5px solid #fff;margin-left:5px;vertical-align:-1px}
.users-mixed{margin-left:auto;padding-right:12px;font-size:11px;color:var(--blue)}
.users-mixed b{color:#fff}
.panel{background:var(--panel)}
.tab{position:absolute;height:35px;line-height:35px;padding:0 14px;font-size:12px;color:#fff}
.tab.active{background:linear-gradient(var(--blue-light),var(--blue));border-radius:3px 3px 0 0}
.inner{position:absolute;background:var(--panel-inner)}
.form-row{position:absolute;left:0;width:620px;height:26px}
.form-row label{position:absolute;right:288px;top:6px;font-size:12px;color:#ddd}
.field{position:absolute;left:341px;width:278px;height:26px;background:var(--field);border:1px solid #777;box-shadow:inset 3px 3px 3px #999}
.captcha{left:341px;top:710px;width:158px;height:66px;background:#fff;border:1px solid #888}
.captcha div{margin:10px 12px;height:42px;background:linear-gradient(90deg,#ddd,#bbb,#ddd)}
.captcha-field{left:341px;top:791px;font-size:12px;color:#555;padding:6px 8px}
.register-btn{left:341px;top:837px;width:104px;height:34px;background:linear-gradient(var(--blue-light),var(--blue));border-radius:3px;color:#fff;font-weight:700;font-size:12px;text-align:center;line-height:34px}
.thumb{position:absolute;width:78px;height:63px;border:1px solid #666}
.movie-meta{position:absolute;left:906px;font-size:12px;line-height:23px}
.movie-meta .author{color:var(--blue);font-weight:700}
.movie-meta small{font-size:11px;color:#fff}
.divider{position:absolute;border-top:1px dotted #777}
.blog-item{position:absolute;left:910px;font-size:12px;line-height:14px;color:#ccc}
.blog-item h4{color:var(--blue);font-size:12px;margin-bottom:5px}
.blog-item small{display:block;margin-top:5px;font-size:9.5px;color:#fff}
</style>
</head>
<body>
<div class="abs topbar">
  <span style="left:119px">Email:</span><div class="top-field" style="left:155px;width:114px"></div>
  <span style="left:288px">Password:</span><div class="top-field" style="left:350px;width:114px"></div>
  <span style="left:483px;font-weight:700;font-size:12px;top:12px">Remember?</span>
  <div class="top-field" style="left:562px;top:14px;width:13px;height:13px"></div>
  <div class="login-btn">LOGIN</div>
  <a style="left:661px;text-decoration:underline">Forgot Password?</a>
  <span style="left:819px">Not a Member Yet?</span>
  <span style="left:928px">Register for your Free Account</span>
</div>

<div class="abs hero" role="img" aria-label="Header artwork of an armed soldier in a tactical helmet"></div>
<div class="abs logo"><span class="logo-mark"></span><span class="logo-name">FRAGVAULT</span></div>
<div class="abs tagline">THE FREE RF:S MIXES SERVICE</div>
<div class="abs search"><div class="search-input">TYPE YOUR SEARCH</div><div class="search-btn">SEARCH</div></div>

<nav class="abs nav">
  <div class="nav-item">HOME</div><div class="nav-item">MIXES</div>
  <div class="nav-item" style="padding:0 25px">RANKING<span class="caret"></span></div>
  <div class="nav-item">AWARDS</div><div class="nav-item">FORUM</div>
  <div class="nav-item">REVIEWS</div><div class="nav-item">MOVIES</div>
  <div class="users-mixed">USERS MIXED: <b>42259</b></div>
</nav>

<section class="abs panel" style="left:110px;top:213px;width:665px;height:687px"></section>
<div class="tab active" style="left:120px;top:223px">REGISTRATION</div>
<div class="inner" style="left:120px;top:258px;width:645px;height:642px"></div>

<div class="form-row" style="top:298px"><label>First-Name:</label><div class="field"></div></div>
<div class="form-row" style="top:339px"><label>Surname:</label><div class="field"></div></div>
<div class="form-row" style="top:380px"><label>Alias:</label><div class="field"></div></div>
<div class="form-row" style="top:421px"><label>E-Mail:</label><div class="field"></div></div>
<div class="form-row" style="top:462px"><label>Password:</label><div class="field"></div></div>
<div class="form-row" style="top:503px"><label>RF:S VaporID:</label><div class="field"></div></div>
<div class="form-row" style="top:544px"><label>RF VaporID:</label><div class="field"></div></div>
<div class="form-row" style="top:586px"><label>RZ VaporID:</label><div class="field"></div></div>
<div class="form-row" style="top:627px"><label>K:S VaporID:</label><div class="field"></div></div>
<div class="form-row" style="top:668px"><label>DOR:S VaporID:</label><div class="field"></div></div>
<div class="form-row" style="top:710px"><label>Word Verification:</label></div>
<div class="abs captcha"><div role="img" aria-label="Distorted verification characters"></div></div>
<svg class="abs" style="left:504px;top:711px" width="15" height="15" viewBox="0 0 15 15"><path d="M3 7a4.5 4.5 0 0 1 8-2.5M12 8a4.5 4.5 0 0 1-8 2.5" fill="none" stroke="#3aa6e0" stroke-width="2"/><path d="M11 1v4H7zM4 14v-4h4z" fill="#3aa6e0"/></svg>
<div class="abs field captcha-field">Please Enter The Text</div>
<div class="abs register-btn">REGISTER</div>

<aside class="abs panel" style="left:790px;top:213px;width:300px;height:296px"></aside>
<div class="tab active" style="left:800px;top:223px">MOVIES</div>
<div class="tab" style="left:872px;top:223px">CALENDER</div>
<div class="inner" style="left:800px;top:258px;width:280px;height:241px"></div>
<div class="thumb" role="img" aria-label="Movie still of a desert map" style="left:815px;top:278px;background:linear-gradient(#b8a684,#7a6a4c)"></div>
<div class="movie-meta" style="top:276px"><div class="author">Author: KestrelNine</div><div>Published: <small>October 14, 2010</small></div><div>Rating: <small>4.5 out of 5</small></div></div>
<div class="divider" style="left:815px;top:361px;width:244px"></div>
<div class="thumb" role="img" aria-label="Movie still of a soldier in a corridor" style="left:815px;top:381px;background:linear-gradient(#a89668,#4e4530)"></div>
<div class="movie-meta" style="top:379px"><div class="author">Author: KestrelNine</div><div>Published: <small>October 14, 2010</small></div><div>Rating: <small>4.5 out of 5</small></div></div>
<div class="divider" style="left:815px;top:464px;width:244px"></div>
<div class="abs" style="left:1000px;top:475px;font-size:12px;font-weight:700;color:#fff">⌖ View All</div>

<aside class="abs panel" style="left:790px;top:524px;width:300px;height:376px"></aside>
<div class="tab active" style="left:800px;top:534px">USERS BLOG</div>
<div class="tab" style="left:906px;top:534px">FORUM</div>
<div class="inner" style="left:800px;top:569px;width:280px;height:331px"></div>
<div class="thumb" role="img" aria-label="Game screenshot of a railway yard" style="left:820px;top:589px;background:linear-gradient(#8a9aa8,#4a4238)"></div>
<div class="blog-item" style="top:587px"><h4>Duis hendrerit elementum</h4>Curabitur euismod is rutum<br>saponec metus velit tepor.<small>October 14, 2010 - 10 Comments</small></div>
<div class="divider" style="left:820px;top:672px;width:241px"></div>
<div class="thumb" role="img" aria-label="Game screenshot of a firefight indoors" style="left:820px;top:693px;background:linear-gradient(#6a5a3c,#2e271a)"></div>
<div class="blog-item" style="top:691px"><h4>Quisque dictum vehicula</h4>Curabitur euismod is rutum<br>saponec metus velit tepor.<small>October 11, 2010 - 22 Comments</small></div>
<div class="divider" style="left:820px;top:776px;width:241px"></div>
<div class="thumb" role="img" aria-label="Game screenshot of a town street" style="left:820px;top:797px;background:linear-gradient(#8e8060,#4a4030)"></div>
<div class="blog-item" style="top:795px"><h4>Quisque dctum vela lorem</h4>Curabitur euismod is rutum<br>saponec metus velit tepor.<small>October 09, 2010 - 13 Comments</small></div>
<div class="divider" style="left:820px;top:880px;width:241px"></div>
</body>
</html>
```